Lawn Company needs design work on a service call flyer!

We are a lawn care company that fertilizes and sprays lawns. This design is meant to be left behind at the customers house after a lawn application has been done too let them know what we have done.

The finished design will be printed on A6 paper (4.1 x 5.8 inches)

I have attached PDF files of the text that I want on the front of the document and the back of the document. I also included a sample design that I had been working on to give some idea what I would like. I don't want the same design, but you can use it as a building block for something new or come up with something entirely different.

FRONT: The front of the design is most important.

BACK: Other then the text the design should be minimal. If possible I would like an outline of the trees in my logo to be a backdrop. I have attached a PDF of the back of my business card as an example

The winning design will be a professional looking document that flows and reflects a lawn care business. Please contact me if you have any questions. I will only pick a design that is better then my current template.

Thank You

Target Market(s)

Lawn Care Customers

Industry/Entity Type

Lawn Care

Requirements
Must have
• 1. Our Logo
• 2. The attached text for the front & back of document
• 3. Our phone number (604-918-4471)
• 4. Our Email address (fenwickturfcare@mailora.net)
Nice to have
• A green theme with flowing graphics
Should not have
• any pictures of houses, people, or tools
• Don't copy the text or design from my design template. It is outdated, is it meant to be an example only

```html
<!DOCTYPE html>
<html lang="en">
<head>
<meta charset="utf-8">
<title>Fenwick Turf Care – Service Call Flyer</title>
<link href="https://fonts.googleapis.com/css2?family=Arimo:ital,wght@0,400;0,700;1,400&display=swap" rel="stylesheet">
<style>
  :root{
    --bg:#e9e6e2;
    --paper:#ffffff;
    --paper-soft:#f5f5f6;
    --green-dark:#0f5a2c;
    --green-mid:#1d8a3c;
    --green-bright:#6cc04a;
    --green-pale:#dcefd2;
    --green-logo:#1f4d22;
    --orange:#e1521f;
    --grey-edge:#b9bcc2;
    --ink:#1b1b1b;
    --ink-soft:#3b3b3b;
    --white:#ffffff;
  }
  *{box-sizing:border-box;margin:0;padding:0}
  html,body{width:1200px;height:927px;overflow:hidden;background:var(--bg)}
  body{font-family:"Arimo",Arial,sans-serif;color:var(--ink);position:relative}
  .sheet{position:absolute;top:67px;width:560px;height:792px;background:var(--paper);overflow:hidden;box-shadow:0 4px 14px rgba(0,0,0,.18)}
  .sheet--front{left:25px;background:var(--paper-soft)}
  .sheet--back{left:615px}
  .sheet svg.art{position:absolute;left:0;width:560px}

  /* front */
  .header-art{top:0;height:240px}
  .brand{position:absolute;left:0;right:0;top:92px;text-align:center;font-weight:700;font-size:42px;letter-spacing:1px;color:var(--green-logo);text-transform:uppercase}
  .form{position:absolute;left:44px;right:40px;top:268px;font-size:14px;line-height:1.2}
  .form p{margin-bottom:20px}
  .form .caps{text-transform:uppercase}
  .blank{display:inline-block;border-bottom:1px solid var(--ink);width:110px;height:1px;vertical-align:baseline;margin:0 4px}
  .blank--long{width:150px}
  .checklist{list-style:none}
  .checklist li{margin-bottom:20px;padding-left:14px;position:relative}
  .checklist li::before{content:"";position:absolute;left:0;top:5px;width:6px;height:6px;background:var(--ink)}
  .pledge{position:absolute;left:44px;right:40px;top:520px;font-size:11px;line-height:1.35;color:var(--ink-soft)}
  .footer-art{bottom:0;height:250px}
  .contact{position:absolute;color:var(--white);font-weight:700}
  .contact .phone{display:block;font-size:32px;letter-spacing:.5px}
  .contact .email{display:block;font-size:21px;font-weight:400;margin-top:4px}
  .sheet--front .contact{left:44px;bottom:52px}

  /* back */
  .guide{position:absolute;left:40px;right:36px;top:36px}
  .guide-title{font-size:17px;font-weight:700;color:var(--green-dark);margin-bottom:22px}
  .guide h2{font-size:22px;font-weight:400;color:var(--green-mid);text-transform:uppercase;letter-spacing:.3px}
  .guide .lead{font-size:10px;color:var(--ink-soft);margin:3px 0 10px}
  .ticks{list-style:none;font-size:9.5px;line-height:1.4;color:var(--ink-soft)}
  .ticks li{position:relative;padding-left:28px;margin-bottom:9px}
  .ticks svg{position:absolute;left:6px;top:2px;width:11px;height:11px}
  .section + .section{margin-top:34px}
  .back-footer-art{bottom:0;height:270px}
  .sheet--back .contact{right:34px;bottom:86px;text-align:right}
</style>
</head>
<body>

<section class="sheet sheet--front" aria-label="Front of flyer">
  <svg class="art header-art" viewBox="0 0 560 240" aria-hidden="true">
    <defs>
      <radialGradient id="headGlow" cx="0.5" cy="0.45" r="0.7">
        <stop offset="0" stop-color="#8fd04e"/>
        <stop offset="0.55" stop-color="#2f9a3c"/>
        <stop offset="1" stop-color="#167a35"/>
      </radialGradient>
    </defs>
    <rect width="560" height="240" fill="url(#headGlow)"/>
    <path d="M0 150 C120 215 330 230 560 210 L560 240 L0 240 Z" fill="var(--grey-edge)"/>
    <path d="M0 156 C120 222 330 236 560 218 L560 240 L0 240 Z" fill="var(--orange)"/>
    <path d="M0 168 C130 232 330 240 560 226 L560 240 L0 240 Z" fill="var(--paper-soft)"/>
  </svg>
  <div class="brand">Fenwick Turf Care</div>

  <div class="form">
    <p class="caps">Application time / date:<span class="blank"></span></p>
    <p class="caps">Your lawn has been professionally serviced today by<span class="blank"></span></p>
    <p>Today’s application consists of</p>
    <ul class="checklist">
      <li>Seasonally Balanced Slow Release Fertilizer</li>
      <li>Broadleaf Weed Control (Please keep off the lawn until it is thoroughly dry)</li>
      <li>Other<span class="blank blank--long"></span></li>
    </ul>
    <p>Please begin watering the lawn<span class="blank"></span>after application</p>
  </div>

  <p class="pledge">“We strive to complete work in a professional manner each and every visit. If you are not satisfied with the level of service you are receiving please contact us. We value your business and wish to maintain long-term relationships with our customers.”</p>

  <svg class="art footer-art" viewBox="0 0 560 250" aria-hidden="true">
    <path d="M0 120 C170 40 420 20 560 60 L560 250 L0 250 Z" fill="var(--green-pale)"/>
    <path d="M0 134 C170 56 420 40 560 80 L560 250 L0 250 Z" fill="var(--green-bright)"/>
    <path d="M0 142 C170 64 420 50 560 92 L560 250 L0 250 Z" fill="var(--orange)"/>
    <path d="M0 152 C170 74 420 62 560 104 L560 250 L0 250 Z" fill="var(--green-dark)"/>
  </svg>
  <div class="contact">
    <span class="phone">604-918-4471</span>
    <span class="email">fenwickturfcare@mailora.net</span>
  </div>
</section>

<section class="sheet sheet--back" aria-label="Back of flyer">
  <svg width="0" height="0" aria-hidden="true" style="position:absolute">
    <symbol id="tick" viewBox="0 0 12 12"><path d="M1 6.5 L4.5 10 L11 2" fill="none" stroke="#1d8a3c" stroke-width="2"/></symbol>
  </svg>
  <div class="guide">
    <p class="guide-title">For best results please follow these general guidelines</p>

    <div class="section">
      <h2>Watering your lawn</h2>
      <p class="lead">When rainfall is not sufficient to meet your lawns watering needs, follow these guidelines for a lush green lawn</p>
      <ul class="ticks">
        <li><svg><use href="#tick"/></svg>Your lawn requires approx. 1 - 1.5 inches of water per week, sometimes more in hot, dry weather</li>
        <li><svg><use href="#tick"/></svg>Avoid short frequent watering. It is best to water deeply once every 5 - 7 days. This encourages deep root growth.</li>
        <li><svg><use href="#tick"/></svg>You can use a Frisbee or an empty tuna can to measure the amount you have watered. Just place it in the path of the sprinkler and when it is full, move your sprinkler to a new location.</li>
        <li><svg><use href="#tick"/></svg>Aerating your lawn once a year will help your lawn utilize more water and prevent unnecessary runoff</li>
      </ul>
    </div>

    <div class="section">
      <h2>Mowing your lawn</h2>
      <p class="lead">Mowing your lawn properly can make all the difference in how it looks throughout the year</p>
      <ul class="ticks">
        <li><svg><use href="#tick"/></svg>You should mow your lawn at 2.5 - 3 inches (no shorter). Mowing at this length helps shade your roots and provides more leaf surface for your lawn to manufacture its own food. As an added bonus it will help your lawn retain its moisture and reduce watering requirements.</li>
        <li><svg><use href="#tick"/></svg>As a general rule, try not to remove more than 1/3 of the leaf blade in a single mowing. During periods of heavy growth, this may mean mowing more frequently than usual.</li>
        <li><svg><use href="#tick"/></svg>Always ensure your lawn mower is maintained and the blade is sharp so that it cuts cleanly.</li>
        <li><svg><use href="#tick"/></svg>Your last mowing in the fall should be shorter, about 2 inches</li>
      </ul>
    </div>
  </div>

  <svg class="art back-footer-art" viewBox="0 0 560 270" aria-hidden="true">
    <path d="M0 270 C40 140 200 50 560 20 L560 270 Z" fill="var(--green-pale)"/>
    <path d="M24 270 C70 160 220 74 560 42 L560 270 Z" fill="var(--green-bright)"/>
    <path d="M32 270 C80 168 230 84 560 52 L560 270 Z" fill="var(--orange)"/>
    <path d="M40 270 C90 176 240 94 560 62 L560 270 Z" fill="var(--green-dark)"/>
  </svg>
  <div class="contact">
    <span class="phone">604-918-4471</span>
    <span class="email">fenwickturfcare@mailora.net</span>
  </div>
</section>

</body>
</html>
```